Business Card for beauty technology startup

Design Glowmi Business Card for a Beauty, based on the website identity and colors (https://www.glowmi-example.com).
Glowmi is a beauty tech startup that gathers helpful product info for beauty lovers and consumers (such as availability on stores, price range and product reviews) for makeup products. The card design must be young, colorful but clean, and very modern.

Target Market(s)

woman, 15-35

Industry/Entity Type

Cosmetics

Contact Information for Business Card

Full Name, address, phone

Font styles to use
Other font styles liked:
• Advent Pro

Colors
e34297
86cfc6
ffffff
5c5c5c
e8e8e8
e667a6
b2b2b2

Requirements
Must have
• One full colored side with a creative design and another with card info
• Use Color palette: #95C5C5 and/or #D38AA5
• Use fonts: Advent Pro
• Use website identity: https://www.glowmi-example.com
Nice to have
• If needed extra font: Roboto

```html
<!DOCTYPE html>
<html lang="en">
<head>
<meta charset="utf-8">
<title>Glowmi Business Card</title>
<link href="https://fonts.googleapis.com/css2?family=Open+Sans:wght@300;400;700&display=swap" rel="stylesheet">
<style>
  :root {
    --backdrop: #e8e8e8;
    --card-black: #161616;
    --rose: #d38aa5;
    --rose-deep: #e34297;
    --teal: #95c5c5;
    --teal-bright: #86cfc6;
    --white: #ffffff;
    --divider: #b2b2b2;
    --grey: #5c5c5c;
  }
  * { margin: 0; padding: 0; box-sizing: border-box; }
  html, body { width: 1200px; height: 864px; overflow: hidden; }
  body {
    background: var(--backdrop);
    font-family: "Open Sans", Arial, sans-serif;
    position: relative;
  }
  .card {
    position: absolute;
    width: 540px;
    height: 308px;
    border-radius: 4px;
    overflow: hidden;
    box-shadow: 0 12px 30px rgba(0,0,0,.22);
  }

  /* colored side */
  .card-back {
    left: 50px; top: 130px;
    background: linear-gradient(135deg, var(--rose) 0%, var(--rose) 45%, var(--teal) 100%);
  }
  .card-back .shape {
    position: absolute; border-radius: 50%;
  }
  .card-back .shape-teal {
    width: 260px; height: 260px; right: -80px; bottom: -120px;
    background: var(--teal-bright); opacity: .55;
  }
  .card-back .shape-rose {
    width: 180px; height: 180px; left: -60px; top: -70px;
    background: var(--rose-deep); opacity: .25;
  }
  .card-back .band {
    position: absolute; left: 0; right: 0; bottom: 0; height: 8px;
    background: linear-gradient(to right, var(--rose-deep), var(--teal-bright));
  }
  .card-back .brand {
    position: absolute; left: 0; right: 0; top: 80px;
    display: flex; flex-direction: column; align-items: center; gap: 14px;
  }
  .brand-dot {
    width: 54px; height: 54px; border-radius: 50%;
    border: 2px solid var(--white);
  }
  .card-back .brand-name {
    font-weight: 300; font-size: 40px; letter-spacing: 9px; padding-left: 9px;
    color: var(--white);
  }
  .card-back .site {
    position: absolute; left: 0; right: 0; top: 232px; text-align: center;
    font-size: 13px; letter-spacing: 5px; color: var(--white);
  }

  /* info side */
  .card-front { left: 610px; top: 426px; background: var(--card-black); }
  .card-front .accent {
    position: absolute; left: 0; right: 0; bottom: 0; height: 6px;
    background: linear-gradient(to right, var(--rose), var(--teal));
  }
  .card-front .brand {
    position: absolute; left: 0; width: 262px; top: 92px;
    display: flex; flex-direction: column; align-items: center; gap: 14px;
  }
  .card-front .brand-dot { border-color: var(--rose); }
  .card-front .brand-name {
    font-weight: 300; font-size: 36px; letter-spacing: 7px; padding-left: 7px;
    color: var(--rose);
  }
  .divider {
    position: absolute; left: 262px; top: 44px; width: 1px; height: 214px;
    background: linear-gradient(to bottom, transparent, var(--teal) 30%, var(--teal) 70%, transparent);
  }
  .details {
    position: absolute; left: 288px; top: 52px; right: 16px; color: var(--white);
    font-size: 13.5px; line-height: 1.45;
  }
  .person-name { color: var(--rose); font-weight: 700; font-size: 14px; }
  .person-title { font-size: 15px; margin-bottom: 8px; }
  .address { margin-bottom: 6px; }
  .contact-list { list-style: none; }
  .contact-list li { display: flex; align-items: center; gap: 8px; white-space: nowrap; }
  .contact-list svg { width: 11px; height: 11px; fill: var(--teal); flex: none; }
</style>
</head>
<body>

<section class="card card-back" aria-label="Card back">
  <span class="shape shape-rose"></span>
  <span class="shape shape-teal"></span>
  <div class="brand">
    <span class="brand-dot"></span>
    <span class="brand-name">GLOWMI</span>
  </div>
  <p class="site">www.glowmi-example.com</p>
  <span class="band"></span>
</section>

<section class="card card-front" aria-label="Card front">
  <div class="brand">
    <span class="brand-dot"></span>
    <span class="brand-name">GLOWMI</span>
  </div>
  <div class="divider"></div>
  <div class="details">
    <p class="person-name">MARA ELLISON</p>
    <p class="person-title">CEO/FOUNDER</p>
    <p class="address">2140 Willow Crest Road<br>Juneau, Alaska 34120</p>
    <ul class="contact-list">
      <li><svg viewBox="0 0 12 12"><path d="M2 1h3l1 3-2 1a7 7 0 0 0 3 3l1-2 3 1v3c0 1-1 1-2 1A10 10 0 0 1 1 3c0-1 0-2 1-2z"/></svg>555 210 4832</li>
      <li><svg viewBox="0 0 12 12"><path d="M3 0h6a1 1 0 0 1 1 1v10a1 1 0 0 1-1 1H3a1 1 0 0 1-1-1V1a1 1 0 0 1 1-1zm0 2v7h6V2z"/></svg>555 318 7604</li>
      <li><svg viewBox="0 0 12 12"><path d="M3 0h6v4H3zM1 5h10v6H1zm2 2v2h6V7z"/></svg>555 472 1956</li>
      <li><svg viewBox="0 0 12 12"><path d="M0 2h12v8H0zm1 1v.5l5 3.5 5-3.5V3z"/></svg>info@glowmi-example.com</li>
      <li><svg viewBox="0 0 12 12"><circle cx="6" cy="6" r="6"/></svg>www.glowmi-example.com</li>
    </ul>
  </div>
  <span class="accent"></span>
</section>

</body>
</html>
```